Webdesign for Dutch IT consultancy company

Make a Wordpress webdesign for a Dutch consultancy company

Briefing Velmora IT

Website for finding and connecting IT-professionals. Corebusiness is to find IT-professionals and to help them to follow their ambitions. We offer training, personal coaching and education trajects.

U can take www.Tralvique.nl as an example for the website.

Home page

U can take www.Tralvique.nl as an example.

There should be jobs on the home page. A block for short info about us and about what whe do and a trigger to contact us quickly.

Jobs Page

On this page should be the jobs that we offer for the professionals. There should be a search function on this page so u can easily find the job that you are looking for.

A call to action can be on this page too.

Also a little block with text for some information.

For professionals page

Block with information on top. Call to action. info about who we work for/with.

For Clients

Info about three different solutions

- Sourcing solutions
- Consultancy solutions
- Custom based traineeships

Request a qoute option

Traineeships page

Info about two different traineeships

- Linux traineeships
- Microsoft traineeships

Call to action/ subscribe for traineeships

About us page

We are Velmora IT

Our mission: Creating cooperations between young professionals and businesses who wanna work on a great future.

Our core values

Last news

Target Market(s)

Young professionals and businesses who need IT services

Industry/Entity Type

It Company

Coding

Coded - Design and coding required

Number of Pages Required

5+ page

Font styles to use
Other font styles liked:
• Calibri

Colors
ffffff
add136
6b449b

Requirements
Must have
• Home page, Jobs Page, Professionals page, Clients page, Traineeships page, About us Page
• Green and/or Purple layout. Job search option, subscribe option
Nice to have
• modern design

```html
<!DOCTYPE html>
<html lang="en">
<head>
<meta charset="utf-8">
<title>Velmora IT – Sourcing and Consultancy</title>
<link href="https://fonts.googleapis.com/css2?family=Lato:wght@400;700;900&display=swap" rel="stylesheet">
<style>
:root{
  --purple:#772a8b;
  --green:#9dc92f;
  --ink:#333333;
  --text:#555555;
  --muted:#777777;
  --light-bg:#eeeeee;
  --line:#dddddd;
  --footer:#2f2f2f;
  --footer-deep:#262626;
  --white:#ffffff;
}
*{box-sizing:border-box;margin:0;padding:0}
html,body{width:1200px;height:3502px;overflow:hidden}
body{font-family:"Lato",Calibri,sans-serif;color:var(--text);background:var(--white);position:relative}
section,header,footer{position:absolute;left:0;width:1200px}
.abs{position:absolute}

/* header */
.site-header{top:0;height:112px;background:var(--white)}
.brand{left:77px;top:36px;font-size:36px;font-weight:900;color:var(--purple);letter-spacing:1px;display:flex;align-items:center;gap:10px}
.brand-dot{width:22px;height:22px;border-radius:50%;background:var(--purple)}
.main-nav{left:383px;right:77px;top:44px;display:flex;justify-content:space-between;font-size:18px;color:#555;letter-spacing:.3px}

/* hero */
.hero{top:112px;height:584px;background:linear-gradient(100deg,#5d5d5d 0%,#8c8c8c 35%,#b9b9b9 65%,#dcdcdc 100%)}
.hero-title{right:77px;top:220px;text-align:right;color:var(--white);font-size:35px;font-weight:700;line-height:52px}
.btn-white{right:77px;top:339px;width:189px;height:46px;background:var(--white);color:var(--purple);font-weight:700;font-size:19px;display:flex;align-items:center;justify-content:center}

/* headings */
.section-title{left:0;width:1200px;text-align:center;font-size:42px;font-weight:700;color:var(--ink)}
.title-rule{left:575px;width:50px;height:3px;background:var(--purple)}

/* welcome */
.welcome{top:696px;height:658px;background:var(--light-bg)}
.welcome .intro{left:159px;width:882px;top:132px;text-align:center;font-size:15.5px;line-height:26px}
.team-photo{left:77px;top:282px;width:437px;height:292px;background:linear-gradient(135deg,#9aa3ad,#5f6770 55%,#c9cfd6)}
.info-item{left:545px;width:578px}
.info-icon{position:absolute;left:0;top:0}
.info-item h3{margin-left:60px;font-size:27px;font-weight:400;color:var(--ink)}
.info-item p{margin-left:60px;margin-top:12px;font-size:15.5px;line-height:26px}

/* jobs */
.jobs{top:1354px;height:771px;background:var(--white)}
.job-table{left:77px;top:147px;width:1046px;border:1px solid var(--line)}
.job-row{position:relative;height:93px;border-bottom:1px solid var(--line)}
.job-row:last-child{border-bottom:none}
.job-row svg{position:absolute;left:28px;top:20px}
.job-name{position:absolute;left:110px;top:22px;font-size:21px;color:#555}
.job-company{position:absolute;left:110px;top:52px;font-size:15.5px;color:#666}
.job-summary{position:absolute;left:425px;top:23px;font-size:15.5px;line-height:26px}
.btn-green{position:absolute;right:38px;top:26px;width:156px;height:42px;background:var(--green);color:var(--white);font-weight:700;font-size:18px;display:flex;align-items:center;justify-content:center}
.btn-purple{background:var(--purple);color:var(--white);font-weight:700;font-size:18px;display:flex;align-items:center;justify-content:center}
.browse{left:511px;top:649px;width:178px;height:47px}

/* quote */
.quote{top:2125px;height:521px;background:linear-gradient(90deg,#f1f4f8 0%,#e3e9f0 50%,#c7d3e0 100%)}
.quote-visual{left:584px;top:0;width:616px;height:521px;background:linear-gradient(120deg,#dbe3ec 0%,#3c5fa8 40%,#23407f 70%,#c9d5e3 100%)}
.quote-title{left:77px;top:72px;font-size:42px;font-weight:400;color:var(--ink)}
.quote-rule{left:77px;top:140px;width:50px;height:3px;background:var(--purple)}
.quote-text{left:77px;top:154px;width:480px;font-size:15px;line-height:26px;color:#555}
.field{background:var(--white);border:1px solid #cfcfcf;font-size:15px;color:#666;padding:12px 14px}
.f-name{left:77px;top:224px;width:220px;height:47px}
.f-phone{left:318px;top:224px;width:217px;height:47px}
.f-msg{left:77px;top:285px;width:458px;height:103px}
.submit{left:77px;top:404px;width:175px;height:44px}

/* blog */
.blog{top:2646px;height:436px;background:var(--white)}
.blog-card{top:133px;width:469px;height:229px;border:1px solid var(--line);background:var(--white)}
.blog-photo{left:0;top:0;width:210px;height:227px;background:linear-gradient(135deg,#c9ccd0,#6d7278 60%,#b0b5bb)}
.date-box{left:145px;top:30px;width:63px;height:98px;background:var(--purple);color:var(--white);text-align:center}
.date-box b{display:block;font-size:33px;font-weight:700;margin-top:12px;line-height:36px}
.date-box span{font-size:16px;font-weight:700}
.blog-body{left:234px;top:28px;width:220px}
.blog-body h4{font-size:20.5px;font-weight:700;color:var(--ink);line-height:28px}
.blog-body p{margin-top:6px;font-size:15.5px;line-height:25px}

/* newsletter */
.newsletter{top:3082px;height:105px;background:var(--purple)}
.newsletter-text{left:79px;top:38px;font-size:24px;font-weight:700;color:var(--white)}
.email-field{left:693px;top:35px;width:292px;height:42px;background:var(--white);font-size:15px;color:#666;padding:12px 14px}
.subscribe{left:997px;top:35px;width:126px;height:42px;background:var(--green);color:var(--white);font-size:18px;display:flex;align-items:center;justify-content:center}

/* footer */
.site-footer{top:3187px;height:250px;background:var(--footer)}
.footer-brand{left:77px;top:76px;font-size:34px;font-weight:900;color:var(--white);letter-spacing:1px}
.social{top:140px;width:38px;height:38px;border-radius:50%;background:var(--white)}
.contact-list{left:846px;top:55px;color:var(--white);font-size:16px;line-height:25px}
.contact-item{position:relative;padding-left:30px;margin-bottom:9px}
.contact-item svg{position:absolute;left:0;top:3px}
.contact-item strong{color:var(--green);font-weight:700}
.copyright{top:3437px;height:65px;background:var(--footer-deep);border-top:1px solid #444;color:#ddd;font-size:15px;display:flex;align-items:center;justify-content:center}
</style>
</head>
<body>

<header class="site-header">
  <div class="abs brand"><span class="brand-dot"></span>VELMORA IT</div>
  <nav class="abs main-nav">
    <span>HOME</span><span>ABOUT US</span><span>JOBS</span><span>PROFESSIONALS</span><span>CLIENTS</span><span>TRAINEESHIPS</span><span>CONTACT</span>
  </nav>
</header>

<section class="hero" role="img" aria-label="Photo of two consultants working together at a laptop in a bright office">
  <h1 class="abs hero-title">VELMORA IT SOURCING AND<br>CONSULTANCY</h1>
  <div class="abs btn-white">CONTACT US</div>
</section>

<section class="welcome">
  <h2 class="abs section-title" style="top:46px">Welcome to Velmora IT</h2>
  <div class="abs title-rule" style="top:112px"></div>
  <p class="abs intro">Lorem ipsum dolor sit amet, consectetur adipiscing elit. Etiam fringilla odio in mollis tincidunt. Morbi tempus purus nisl, a mattis turpis maximus non. Suspendisse semper posuere sapien sit amet dignissim. Etiam et quam ut ex varius eleifend eget nec purus. Suspendisse eget lorem nulla. Aenean et ullamcorper mauris.</p>
  <div class="abs team-photo" role="img" aria-label="Photo of a business team gathered around a laptop in a meeting"></div>
  <div class="abs info-item" style="top:308px">
    <svg class="info-icon" width="44" height="44" viewBox="0 0 44 44" fill="none" stroke="#333" stroke-width="2.2"><circle cx="16" cy="14" r="7"/><path d="M3 38c1-9 7-14 13-14s11 4 12 10"/><circle cx="36" cy="5" r="1.5" fill="#333"/><path d="M36 11v13"/></svg>
    <h3>About Us</h3>
    <p>Lorem ipsum dolor sit amet, consectetur adipiscing elit. Etiam fringilla odio in mollis tincidunt. Morbi tempus purus nisl, a mattis turpis maximus non.</p>
  </div>
  <div class="abs info-item" style="top:455px">
    <svg class="info-icon" width="44" height="44" viewBox="0 0 44 44" fill="none" stroke="#333" stroke-width="2.2"><rect x="7" y="6" width="26" height="34" rx="3"/><rect x="14" y="2" width="12" height="7" rx="2"/><path d="M13 24l5 5 10-10"/></svg>
    <h3>What We Do</h3>
    <p>Lorem ipsum dolor sit amet, consectetur adipiscing elit. Etiam fringilla odio in mollis tincidunt. Morbi tempus purus nisl, a mattis turpis maximus non.</p>
  </div>
</section>

<section class="jobs">
  <h2 class="abs section-title" style="top:40px;color:#555">Job Posts</h2>
  <div class="abs title-rule" style="top:106px"></div>
  <div class="abs job-table">
    <div class="job-row">
      <svg width="54" height="54" viewBox="0 0 54 54" fill="none" stroke="#9dc92f" stroke-width="5"><rect x="4" y="8" width="40" height="40" rx="3"/><path d="M14 26l10 10 24-28"/></svg>
      <span class="job-name">Graphic Designer</span><span class="job-company">Nordalis</span>
      <p class="job-summary">Lorem ipsum dolor sit amet,<br>consectetur adipiscing elit.</p>
      <span class="btn-green">KNOW MORE</span>
    </div>
    <div class="job-row">
      <svg width="54" height="54" viewBox="0 0 54 54" fill="none" stroke="#9dc92f" stroke-width="5"><rect x="4" y="8" width="40" height="40" rx="3"/><path d="M14 26l10 10 24-28"/></svg>
      <span class="job-name">Graphic Designer</span><span class="job-company">Nordalis</span>
      <p class="job-summary">Lorem ipsum dolor sit amet,<br>consectetur adipiscing elit.</p>
      <span class="btn-green">KNOW MORE</span>
    </div>
    <div class="job-row">
      <svg width="54" height="54" viewBox="0 0 54 54" fill="none" stroke="#9dc92f" stroke-width="5"><rect x="4" y="8" width="40" height="40" rx="3"/><path d="M14 26l10 10 24-28"/></svg>
      <span class="job-name">Graphic Designer</span><span class="job-company">Nordalis</span>
      <p class="job-summary">Lorem ipsum dolor sit amet,<br>consectetur adipiscing elit.</p>
      <span class="btn-green">KNOW MORE</span>
    </div>
    <div class="job-row">
      <svg width="54" height="54" viewBox="0 0 54 54" fill="none" stroke="#9dc92f" stroke-width="5"><rect x="4" y="8" width="40" height="40" rx="3"/><path d="M14 26l10 10 24-28"/></svg>
      <span class="job-name">Graphic Designer</span><span class="job-company">Nordalis</span>
      <p class="job-summary">Lorem ipsum dolor sit amet,<br>consectetur adipiscing elit.</p>
      <span class="btn-green">KNOW MORE</span>
    </div>
    <div class="job-row">
      <svg width="54" height="54" viewBox="0 0 54 54" fill="none" stroke="#9dc92f" stroke-width="5"><rect x="4" y="8" width="40" height="40" rx="3"/><path d="M14 26l10 10 24-28"/></svg>
      <span class="job-name">Graphic Designer</span><span class="job-company">Nordalis</span>
      <p class="job-summary">Lorem ipsum dolor sit amet,<br>consectetur adipiscing elit.</p>
      <span class="btn-green">KNOW MORE</span>
    </div>
  </div>
  <div class="abs btn-purple browse">BROWSE MORE</div>
</section>

<section class="quote">
  <div class="abs quote-visual" role="img" aria-label="Photo of a businessman in a blue suit adjusting his cuff, blended with a city skyline"></div>
  <h2 class="abs quote-title">Request a Quick Quote</h2>
  <div class="abs quote-rule"></div>
  <p class="abs quote-text">Please feel free to contact us at the information provided below and we will be sure to get back to you as soon as possible.</p>
  <div class="abs field f-name">Name</div>
  <div class="abs field f-phone">Phone No.</div>
  <div class="abs field f-msg">Message</div>
  <div class="abs btn-purple submit">SUBMIT</div>
</section>

<section class="blog">
  <h2 class="abs section-title" style="top:40px">Latest Blog</h2>
  <div class="abs title-rule" style="top:97px"></div>
  <article class="abs blog-card" style="left:98px">
    <div class="abs blog-photo" role="img" aria-label="Photo of a businessman in a suit at an office desk"></div>
    <div class="abs date-box"><b>29</b><span>APR</span></div>
    <div class="abs blog-body">
      <h4>Lorem Ipsum is simply dummy text.</h4>
      <p>Lorem Ipsum is simply dummy text of the printing and typesetting industry. Lorem Ipsum has been the industry's standard dummy.</p>
    </div>
  </article>
  <article class="abs blog-card" style="left:633px">
    <div class="abs blog-photo" role="img" aria-label="Photo of colleagues in a bright meeting room"></div>
    <div class="abs date-box" style="top:128px"><b>29</b><span>APR</span></div>
    <div class="abs blog-body">
      <h4>Lorem Ipsum is simply dummy text.</h4>
      <p>Lorem Ipsum is simply dummy text of the printing and typesetting industry. Lorem Ipsum has been the industry's standard dummy.</p>
    </div>
  </article>
</section>

<section class="newsletter">
  <p class="abs newsletter-text">To get latest updates and promotions signup now!</p>
  <div class="abs email-field">Enter Your Email</div>
  <div class="abs subscribe">SUBSCRIBE</div>
</section>

<footer class="site-footer">
  <div class="abs footer-brand">VELMORA IT</div>
  <span class="abs social" style="left:135px"></span>
  <span class="abs social" style="left:186px"></span>
  <span class="abs social" style="left:235px"></span>
  <div class="abs contact-list">
    <div class="contact-item">
      <svg width="18" height="22" viewBox="0 0 18 22" fill="#fff"><path d="M9 0a8 8 0 0 0-8 8c0 6 8 14 8 14s8-8 8-14a8 8 0 0 0-8-8zm0 11a3 3 0 1 1 0-6 3 3 0 0 1 0 6z"/></svg>
      <strong>VELMORA IT</strong><br>Lorem ipsum dolor sit amet,<br>consectetur adipiscing elit.
    </div>
    <div class="contact-item">
      <svg width="18" height="18" viewBox="0 0 24 24" fill="#fff"><path d="M6.6 10.8a15 15 0 0 0 6.6 6.6l2.2-2.2a1 1 0 0 1 1-.25 11 11 0 0 0 3.6.6 1 1 0 0 1 1 1V20a1 1 0 0 1-1 1A17 17 0 0 1 3 4a1 1 0 0 1 1-1h3.5a1 1 0 0 1 1 1c0 1.25.2 2.45.6 3.6a1 1 0 0 1-.25 1z"/></svg>
      123 456 7890
    </div>
    <div class="contact-item">
      <svg width="18" height="16" viewBox="0 0 18 14" fill="none" stroke="#fff" stroke-width="1.8"><rect x="1" y="1" width="16" height="12"/><path d="M1 1l8 7 8-7"/></svg>
      info@velmorait.com
    </div>
  </div>
</footer>

<div class="abs copyright" style="left:0;width:1200px">©VELMORA IT- 2017. All Rights Reserved.</div>

</body>
</html>
```